Restful Path Network South Australia Booklet and Resource cover design for use on various inhouse

We need a design using the attached art and logo which can be used in all inhouse brochure and booklet production so that we can assume a common image and look across all of our productions
Updates

Thanks for your designs.  I have posted them for voting with my staff and Board sub committee.  Is it possible to see some landscape versions.

Target Market(s)

People newly diagnosed with a terminal illness, health professionals caring for people with a terminal illness. family of people affected by terminal illness. Age 18-100, Male and female.

Industry/Entity Type

Council

Requirements
Must have
• The restful path network of SA Logo
• The integration of the Aboriginal artwork into the design

```html
<!DOCTYPE html>
<html lang="en">
<head>
<meta charset="utf-8">
<title>Terminal Illness – Restful Path Network SA</title>
<link href="https://fonts.googleapis.com/css2?family=Josefin+Sans:wght@400;700&display=swap" rel="stylesheet">
<style>
  :root {
    --art-olive: #6d5a2c;
    --art-ochre: #8a6d32;
    --art-maroon: #6e2f2c;
    --panel-fill: #d7cdc3;
    --panel-frame: #ffffff;
    --title-ink: #44222e;
    --subtitle-ink: #9a4b3b;
    --badge-fill: #ffffff;
    --badge-ink: #2b8fb8;
  }
  * { margin: 0; padding: 0; box-sizing: border-box; }
  html, body {
    width: 1200px;
    height: 800px;
    overflow: hidden;
    background: var(--art-olive);
  }
  .cover {
    position: relative;
    width: 1200px;
    height: 800px;
    overflow: hidden;
    font-family: "Josefin Sans", sans-serif;
  }
  .cover__artwork {
    position: absolute;
    inset: 0;
    background:
      radial-gradient(circle at 20% 30%, rgba(110, 47, 44, 0.55), transparent 45%),
      radial-gradient(circle at 80% 70%, rgba(110, 47, 44, 0.5), transparent 45%),
      linear-gradient(135deg, var(--art-ochre), var(--art-olive));
  }
  .title-panel {
    position: absolute;
    left: 92px;
    top: 97px;
    width: 1017px;
    height: 528px;
    background: var(--panel-fill);
    border: 6px solid var(--panel-frame);
    text-align: center;
  }
  .title-panel__heading {
    color: var(--title-ink);
    font-weight: 700;
    text-transform: uppercase;
  }
  .title-panel__line {
    position: absolute;
    left: 0;
    right: 0;
    font-size: 137px;
    line-height: 1;
    letter-spacing: 0.04em;
    padding-left: 0.04em;
  }
  .title-panel__line--first { top: 57px; }
  .title-panel__line--second { top: 215px; }
  .title-panel__subtitle {
    position: absolute;
    left: 0;
    right: 0;
    top: 364px;
    color: var(--subtitle-ink);
    font-weight: 400;
    font-size: 34px;
    line-height: 67px;
    letter-spacing: 0.03em;
  }
  .network-badge {
    position: absolute;
    left: 492px;
    top: 675px;
    width: 216px;
    height: 58px;
    background: var(--badge-fill);
    display: flex;
    align-items: center;
    justify-content: center;
    gap: 8px;
    padding: 0 8px;
  }
  .network-badge__dot {
    width: 14px;
    height: 14px;
    border-radius: 50%;
    background: var(--badge-ink);
    flex: none;
  }
  .network-badge__name {
    color: var(--badge-ink);
    font-weight: 700;
    font-size: 15px;
    line-height: 1.15;
  }
</style>
</head>
<body>
  <main class="cover">
    <div class="cover__artwork" role="img" aria-label="Aboriginal dot artwork in olive, ochre and maroon with repeating flower motifs"></div>

    <section class="title-panel">
      <h1 class="title-panel__heading">
        <span class="title-panel__line title-panel__line--first">Terminal</span>
        <span class="title-panel__line title-panel__line--second">Illness</span>
      </h1>
      <p class="title-panel__subtitle">Health Professionals Caring<br>For People With A Terminal Illness</p>
    </section>

    <div class="network-badge">
      <span class="network-badge__dot"></span>
      <span class="network-badge__name">Restful Path<br>Network SA</span>
    </div>
  </main>
</body>
</html>
```